Business Card design

I would like to redo the business cards we have. I want a group card and then individual cards made for each doctor. I like the format of the card attached.

```html
<!DOCTYPE html>
<html lang="en">
<head>
<meta charset="utf-8">
<title>Harbor Valley Cancer Care – Business Cards</title>
<link rel="stylesheet" href="https://fonts.googleapis.com/css2?family=Roboto:wght@400;500;700&display=swap">
<style>
  :root {
    --backdrop: #a6a8ac;
    --card: #ffffff;
    --brand-dark: #0e5a85;
    --brand-blue: #2b9dd4;
    --ink: #58595b;
    --on-blue: #ffffff;
  }
  * { box-sizing: border-box; margin: 0; padding: 0; }
  html, body { width: 1200px; height: 2400px; overflow: hidden; }
  body {
    background: var(--backdrop);
    font-family: "Roboto", Arial, sans-serif;
    position: relative;
  }
  .card {
    position: absolute;
    left: 140px;
    width: 920px;
    height: 528px;
    background: var(--card);
    border-radius: 24px;
    box-shadow: 6px 8px 10px rgba(0,0,0,0.35);
    overflow: hidden;
  }
  .card--one { top: 94px; }
  .card--two { top: 674px; }
  .card--three { top: 1247px; }
  .card--group { top: 1820px; }

  .brand {
    display: flex;
    align-items: center;
    gap: 22px;
    color: var(--brand-dark);
    font-weight: 700;
  }
  .brand__dot {
    width: 84px; height: 84px;
    border-radius: 50%;
    background: var(--brand-blue);
    flex: none;
  }
  .brand__name { line-height: 1.02; }
  .brand__line1 { display: block; font-size: 62px; }
  .brand__line2 { display: block; font-size: 46px; }

  .doctor .brand {
    position: absolute;
    top: 96px;
    left: 0; right: 0;
    justify-content: center;
  }
  .doctor__name {
    position: absolute;
    top: 304px;
    left: 0; right: 0;
    text-align: center;
    font-size: 38px;
    font-weight: 700;
    color: var(--ink);
    letter-spacing: 0.5px;
  }
  .doctor__contact {
    position: absolute;
    top: 366px;
    left: 0; right: 0;
    display: flex;
    justify-content: center;
    gap: 56px;
    font-size: 27px;
    color: var(--ink);
  }
  .contact-item { display: flex; align-items: center; gap: 10px; }
  .icon { width: 28px; height: 24px; fill: currentColor; flex: none; }

  .group__front {
    position: absolute;
    left: 0; top: 0; bottom: 0;
    width: 410px;
    display: flex;
    align-items: center;
    padding-left: 26px;
  }
  .group__front .brand { gap: 12px; }
  .group__front .brand__dot { width: 52px; height: 52px; }
  .group__front .brand__line1 { font-size: 40px; }
  .group__front .brand__line2 { font-size: 29px; }
  .group__rule {
    position: absolute;
    left: 410px; top: 0; bottom: 0;
    width: 12px;
    background: var(--brand-dark);
  }
  .group__locations {
    position: absolute;
    left: 422px; right: 0; top: 0; bottom: 0;
    background: var(--brand-blue);
    color: var(--on-blue);
    padding: 22px 18px 0 20px;
  }
  .location { padding-bottom: 16px; }
  .location + .location {
    border-top: 2px solid var(--on-blue);
    padding-top: 16px;
  }
  .location__address {
    font-size: 20px;
    line-height: 31px;
    letter-spacing: 1px;
  }
  .location__phones { margin-top: 6px; font-size: 15px; line-height: 25px; letter-spacing: 0.5px; }
  .location__phones .contact-item { gap: 12px; }
  .location__phones .icon { width: 17px; height: 14px; }
</style>
</head>
<body>
  <svg width="0" height="0" style="position:absolute" aria-hidden="true">
    <symbol id="icon-phone" viewBox="0 0 28 24">
      <path d="M2 8c0-4 6-6 12-6s12 2 12 6v3h-6V8c-2-1-10-1-12 0v3H2z"/>
      <path d="M7 12l3-4h8l3 4v10H7z"/>
      <g fill="#fff"><rect x="10" y="13" width="2" height="2"/><rect x="13" y="13" width="2" height="2"/><rect x="16" y="13" width="2" height="2"/><rect x="10" y="17" width="2" height="2"/><rect x="13" y="17" width="2" height="2"/><rect x="16" y="17" width="2" height="2"/></g>
    </symbol>
    <symbol id="icon-fax" viewBox="0 0 28 24">
      <rect x="7" y="0" width="14" height="7"/>
      <rect x="1" y="8" width="26" height="10" rx="2"/>
      <rect x="6" y="14" width="16" height="10" fill="#fff" stroke="currentColor" stroke-width="2"/>
      <rect x="9" y="18" width="10" height="2"/>
    </symbol>
  </svg>

  <section class="card card--one doctor">
    <div class="brand">
      <span class="brand__dot"></span>
      <span class="brand__name"><span class="brand__line1">Harbor Valley</span><span class="brand__line2">Cancer Care, PA</span></span>
    </div>
    <h2 class="doctor__name">Priya Ramanathan, M.D.</h2>
    <div class="doctor__contact">
      <span class="contact-item"><svg class="icon"><use href="#icon-phone"/></svg>(917) 555-0142</span>
    </div>
  </section>

  <section class="card card--two doctor">
    <div class="brand">
      <span class="brand__dot"></span>
      <span class="brand__name"><span class="brand__line1">Harbor Valley</span><span class="brand__line2">Cancer Care, PA</span></span>
    </div>
    <h2 class="doctor__name">Amina Qureshi, M.D.</h2>
    <div class="doctor__contact">
      <span class="contact-item"><svg class="icon"><use href="#icon-phone"/></svg>(908) 555-0117</span>
      <span class="contact-item"><svg class="icon"><use href="#icon-fax"/></svg>(908) 555-0146</span>
    </div>
  </section>

  <section class="card card--three doctor">
    <div class="brand">
      <span class="brand__dot"></span>
      <span class="brand__name"><span class="brand__line1">Harbor Valley</span><span class="brand__line2">Cancer Care, PA</span></span>
    </div>
    <h2 class="doctor__name">Karim B. Haddad, M.D.</h2>
    <div class="doctor__contact">
      <span class="contact-item"><svg class="icon"><use href="#icon-phone"/></svg>(908) 555-0117</span>
      <span class="contact-item"><svg class="icon"><use href="#icon-fax"/></svg>(908) 555-0146</span>
    </div>
  </section>

  <section class="card card--group">
    <div class="group__front">
      <div class="brand">
        <span class="brand__dot"></span>
        <span class="brand__name"><span class="brand__line1">Harbor Valley</span><span class="brand__line2">Cancer Care, PA</span></span>
      </div>
    </div>
    <div class="group__rule"></div>
    <div class="group__locations">
      <div class="location">
        <p class="location__address">40 Orchard Park Road, Suite 200<br>Fairview, New Jersey 07100</p>
        <div class="location__phones">
          <div class="contact-item"><svg class="icon"><use href="#icon-phone"/></svg>(973) 555-0180</div>
          <div class="contact-item"><svg class="icon"><use href="#icon-fax"/></svg>(973) 555-0150</div>
        </div>
      </div>
      <div class="location">
        <p class="location__address">Linden Hollis Ambulatory Care Pavilion<br>12 Cove Avenue, Suite 2<br>Westbrook, New Jersey 07040</p>
        <div class="location__phones">
          <div class="contact-item"><svg class="icon"><use href="#icon-phone"/></svg>(973) 555-0100</div>
          <div class="contact-item"><svg class="icon"><use href="#icon-fax"/></svg>(973) 555-0134</div>
        </div>
      </div>
      <div class="location">
        <p class="location__address">318 West Maple Avenue<br>Millbrook, New Jersey 07200</p>
        <div class="location__phones">
          <div class="contact-item"><svg class="icon"><use href="#icon-phone"/></svg>(908) 555-0117</div>
          <div class="contact-item"><svg class="icon"><use href="#icon-fax"/></svg>(908) 555-0146</div>
        </div>
      </div>
    </div>
  </section>
</body>
</html>
```